Wordpress Design for Financial Trading Software

Our Software QuantoMesh allows clients to program their trading strategy and use it to trade automatically on stock markets. For further details please visit our preliminary / draft web page: http://www.quantomesh-example.ch/wordpress.
We would like the Web Page to represent the following values:
- Innovative
- High Tech
- High Quality
- Professional
- Sophisticated
- State-of-the-art
- Modern
- Versatile
We need a Design based on a PSD file for the Main Page containing the following:
Header:
- Logo + optional Image / Graphic / Slogan / Quote
- Menu Bar with drop-down for Sub-Menus
- Search Box
Full Width Featured Content Area
- Main Description of the Product (with read-more Link + optional Image / Graphic)
Smaller Featured Content Areas:
- Product Features (with read-more Link + optional Icon)
- Documentation and Demo (with read-more Link + optional Icon)
- Professional Services (with read-more Link + optional Icon)
- Training (with read-more Link + optional Icon)
Latest News:
- 3-5 latest News + option Image / Grafic
Testimonial:
- 1 Customer Testimonial with Photo
Footer:
- Copyright and "all rights reserved" Notice
- Privacy Policy
- Contact Info: Address, Phone Number and Email
- Link to Site-Map
- Social Media Connectors (Chatterwall, CareerWeave, RSS Feed & Email)
Guidelines for Style/Theme:
- Well structured, Lean, Easy-to-use Page
- Use of existing Logo
- Sans-Serif Fonts
- Colors matching our Logo (not too many Colors)
- Main Focus: Desktop-Computers.
- However: Page should be readable on mobile Devices also
- Please show one element of the navigation bar in selected state with drop-down
- After the contest we will work with the Designer on the other Pages
- We will need a PSD File, so that we can organize the actual coding of the Wordpress Page / Theme
- If images / photos are used, they have to be royalty-free.
Example Pages that we like:
http://www.brindlecove.example/
http://www.hqz.example/
http://www.mockturn.example/
http://www.marketloft.example/
http://www.nimbravault.example/
http://www.shelfgrid.example/
http://www.pme-werkplatz.example.ch/
https://www.o-volving.example/
http://www.dealharbor.example/
https://sketchrally.example/web-design/contests/green-power-ventures-exchange-portal-website-design-402817/entries/38172640
https://sketchrally.example/web-design/contests/website-design-wanted-halvex-holdings-57210/entries/6431872
http://files.artpooling.example/design_img/482917/37650/37650_2948301_482917_image.jpg
WordPress Plugins currently in use:
- Quick Safe Inquiry Box
- Glowpane Album
- PinTrail Simple Terrain Charts
Reason: A few Designers let us know, that they need more time to work on their Designs. We are in no rush and would like to see as many good Designs as possible!
Target Market(s)
Investment Banks and Hedge Funds
Industry/Entity Type
Trade

```html
<!DOCTYPE html>
<html lang="en">
<head>
<meta charset="utf-8">
<title>QuantoMesh – Algorithmic Trading Platform</title>
<link rel="stylesheet" href="https://fonts.googleapis.com/css2?family=Source+Sans+3:ital,wght@0,400;0,600;0,700;1,400&display=swap">
<style>
:root{
  --gold:#c7b887;
  --gold-light:#ddd3ae;
  --gold-text:#b5a265;
  --olive:#9c8a4f;
  --slate:#6b7883;
  --slate-dark:#5d6973;
  --footer:#67737d;
  --ink:#333;
  --muted:#555;
  --rule:#e3e3e3;
  --white:#fff;
}
*{box-sizing:border-box;margin:0;padding:0}
html,body{width:747px;height:1200px;overflow:hidden;background:var(--white)}
body{position:relative;font-family:"Source Sans 3",Arial,sans-serif;color:var(--ink)}
.abs{position:absolute}
.topline{left:0;top:0;width:747px;height:2px;background:var(--gold)}
.brand{left:80px;top:30px;display:flex;align-items:center;gap:7px;font-size:24px;font-weight:600;color:var(--slate-dark)}
.brand-mark{width:16px;height:16px;background:var(--gold)}
.callus{right:68px;top:10px;font-size:14.5px;color:#777;text-align:right}
.emailus{right:70px;top:28px;font-size:10.5px;color:#777}
.search{left:542px;top:50px;width:136px;height:21px;border:1px solid #ddd;border-radius:3px;font-size:7px;color:#888;padding:6px 9px;box-shadow:0 1px 2px rgba(0,0,0,.1)}
.search svg{position:absolute;right:6px;top:4px}
.nav{left:0;top:77px;width:747px;height:33px;background:linear-gradient(#e2d9b9,#c9bc8d);border-bottom:1px solid #b8a978}
.nav ul{list-style:none;display:flex;position:absolute;left:72px;top:0;height:33px}
.nav li{font-size:10.5px;color:#3a3a3a;padding:0 8px;line-height:33px;white-space:nowrap}
.nav li.active{background:var(--slate);color:var(--white);padding:0 7px}
.nav li.open{background:var(--white);color:#444;padding:0 5px}
.dropdown{left:272px;top:110px;width:106px;height:69px;background:var(--white);box-shadow:0 2px 3px rgba(0,0,0,.15);padding:8px 8px;z-index:3}
.dropdown p{font-size:8px;line-height:18.5px;color:#222}
.hero{left:0;top:110px;width:747px;height:282px;background:radial-gradient(ellipse at 30% 40%,#7c8891,var(--slate) 70%)}
.hero-art{left:100px;top:60px;width:300px;height:200px;border-radius:10px;background:radial-gradient(ellipse,#d9e0e4,rgba(180,192,200,.4) 60%,transparent 75%)}
.hero h1{left:412px;top:66px;font-size:16px;font-weight:600;color:var(--white);letter-spacing:.2px}
.hero p{left:412px;top:94px;width:212px;font-size:12px;line-height:15.3px;color:var(--white);text-align:justify}
.more{left:411px;top:170px;width:100px;height:26px;border-radius:3px;background:linear-gradient(#fafafa,#dedede);font-size:11px;color:#666;text-align:center;line-height:26px}
.strip{left:0;top:392px;width:747px;height:62px;background:linear-gradient(#fff,#ececec 60%,#fff)}
.strip-shadow{left:60px;top:452px;width:627px;height:3px;background:radial-gradient(ellipse,#bdbdbd,transparent 70%)}
.partner{height:18px;border-radius:3px;background:#b9b9b9;top:416px}
.about h2,.col h2{font-size:12.5px;font-weight:600;color:#444}
.about-text{left:76px;top:488px;width:407px;font-size:8.2px;line-height:15px;color:#333;text-align:justify}
.about-img{left:496px;top:470px;width:168px;height:97px;border:3px solid #6e7a84;background:linear-gradient(135deg,#dbe9f5,#6aa3d6 45%,#2d5d8c)}
.divider{width:1px;background:linear-gradient(#fff,var(--rule),#fff)}
.bullets{list-style:none}
.bullets li{position:relative;padding-left:11px;font-size:8.2px;color:#333}
.bullets li::before{content:"›";position:absolute;left:0;top:-1px;color:#666}
.small{font-size:8.2px;line-height:13.5px;color:#333;text-align:justify}
.video{left:288px;top:609px;width:169px;height:98px;border:3px solid #ddd;background:linear-gradient(#141c4a,#2c3a84 60%,#1c285e)}
.play{left:64px;top:33px;width:32px;height:32px;border-radius:50%;background:rgba(0,0,0,.55)}
.testi p{font-size:8.2px;line-height:17.5px;color:#222;width:120px}
.testi .who{font-style:italic;color:#999;font-size:8px;line-height:12px}
.photo{width:56px;height:56px;border:2px solid #fff;box-shadow:0 0 2px rgba(0,0,0,.35);background:linear-gradient(#d9e5ef,#9fb7cc)}
.lower h2{font-size:13px;font-weight:400;color:#444}
.btn{width:63px;height:20px;border-radius:2px;background:linear-gradient(#d6cb9f,#b8a872);color:#fff;font-size:7.5px;font-weight:600;text-align:center;line-height:20px}
.news{left:93px;top:981px;width:562px;height:45px;background:linear-gradient(#ededed,#e0e0e0);border-radius:2px}
.news h3{position:absolute;left:14px;top:13px;font-size:15px;font-weight:400;color:#333}
.news .date{position:absolute;left:110px;top:7px;width:30px;height:30px;border-radius:50%;background:#fff;font-size:7px;text-align:center;line-height:9px;padding-top:6px;color:#444}
.news p{position:absolute;left:139px;top:9px;width:410px;font-size:7.8px;line-height:14.5px;color:#555}
.footer{left:0;top:1032px;width:747px;height:168px;background:var(--footer)}
.f-head{font-size:9px;color:var(--gold-light)}
.f-item{font-size:7.2px;color:#eee}
.f-list p{font-size:7.2px;color:#eee;line-height:15px}
.f-brand{left:546px;top:1050px;display:flex;align-items:center;gap:6px;font-size:18px;font-weight:600;color:#fff}
.f-mark{width:12px;height:12px;background:#fff}
.f-copy{left:546px;top:1109px;font-size:7.2px;line-height:12.5px;color:#d6dbde}
.soc{width:16px;height:16px;border-radius:50%;background:#7f8a93;top:1150px}
</style>
</head>
<body>
<div class="abs topline"></div>

<header>
  <div class="abs brand"><span class="brand-mark"></span>QuantoMesh</div>
  <div class="abs callus">Call Us : 1-800-414 7720</div>
  <div class="abs emailus">Email us : info@quantomesh-example.com</div>
  <div class="abs search">Search
    <svg width="12" height="12" viewBox="0 0 12 12"><circle cx="5" cy="5" r="3.5" fill="none" stroke="#666" stroke-width="1.2"/><path d="M7.6 7.6 11 11" stroke="#666" stroke-width="1.4"/></svg>
  </div>
  <nav class="abs nav">
    <ul>
      <li class="active">HOME</li>
      <li>PRODUCT</li>
      <li>DOCUMENTATION</li>
      <li class="open">SERVICES &amp; SUPPORT</li>
      <li>CLIENTS &amp; PARTNERS</li>
      <li>NEWS</li>
      <li>ABOUT US</li>
      <li>CONTACT &amp; SALES</li>
    </ul>
  </nav>
  <div class="abs dropdown">
    <p>» &nbsp;Professional Services</p>
    <p>» &nbsp;Training</p>
    <p>» &nbsp;Forum</p>
  </div>
</header>

<section class="abs hero">
  <div class="abs hero-art" role="img" aria-label="Illustration of traders connected on a network of hexagon tiles"></div>
  <svg class="abs" style="left:86px;top:100px" width="26" height="44" viewBox="0 0 26 44"><path d="M22 3 4 22l18 19" fill="none" stroke="#fff" stroke-width="4"/></svg>
  <svg class="abs" style="left:646px;top:100px" width="26" height="44" viewBox="0 0 26 44"><path d="M4 3l18 19L4 41" fill="none" stroke="#fff" stroke-width="4"/></svg>
  <h1 class="abs">QUANTOMESH</h1>
  <p class="abs">Server based Algorithmic Trading Platform that enables development, simulation and execution of multiple strategies in parallel.</p>
  <div class="abs more">MORE DETAILS</div>
</section>

<section aria-label="Partners">
  <div class="abs strip"></div>
  <svg class="abs" style="left:64px;top:419px" width="12" height="10" viewBox="0 0 12 10"><path d="M5 1 1 5l4 4M10 1 6 5l4 4" fill="none" stroke="#333" stroke-width="1.4"/></svg>
  <svg class="abs" style="left:668px;top:419px" width="12" height="10" viewBox="0 0 12 10"><path d="M2 1l4 4-4 4M7 1l4 4-4 4" fill="none" stroke="#333" stroke-width="1.4"/></svg>
  <div class="abs partner" style="left:114px;width:58px"></div>
  <div class="abs partner" style="left:192px;width:68px"></div>
  <div class="abs partner" style="left:281px;width:80px"></div>
  <div class="abs partner" style="left:380px;width:54px"></div>
  <div class="abs partner" style="left:453px;width:68px"></div>
  <div class="abs partner" style="left:537px;width:98px"></div>
  <div class="abs strip-shadow"></div>
</section>

<section class="about">
  <h2 class="abs" style="left:75px;top:466px">QUANTOMESH</h2>
  <p class="abs about-text">QuantoMesh is a Server based Algorithmic Trading Platform that enables development, simulation and execution of multiple strategies in parallel. QuantoMesh is built on Event Driven Architecture (EDA) and therefore accommodates strategies that are predominantly time-based and cannot be programed with traditional procedural programming languages. QuantoMesh is extensible and fully customizable for situations where strategy specific functionality is required. Full access to the Source Code of the System is provided. QuantoMesh is an all-in-one solution for investment banks, quantitative hedge funds and proprietary trading groups.</p>
  <div class="abs about-img" role="img" aria-label="Photo of a businessman facing floating data screens"></div>
</section>

<section class="col">
  <h2 class="abs" style="left:74px;top:592px">Our Features</h2>
  <ul class="abs bullets" style="left:78px;top:619px;width:166px;line-height:16.2px">
    <li style="text-align:justify">Automate Trading Strategies based on Complex Trading Rules</li>
    <li style="text-align:justify">Development, Simulation and Live Trading of several strategies in parallel</li>
    <li style="text-align:justify">Multiple Broker Interfaces and Multiple Market Data Providers</li>
    <li style="text-align:justify">Support for wide array of security types and asset classes</li>
  </ul>
  <p class="abs small" style="left:79px;top:752px;width:169px">Duis ut justo lorem. Suspendisse eleifend, magna non sollicitudin tincidunt, urna mauris adipiscing mauris, eget eleifend magna elit eu</p>
  <div class="abs divider" style="left:270px;top:590px;height:225px"></div>

  <h2 class="abs" style="left:286px;top:590px">Our Products</h2>
  <div class="abs video" role="img" aria-label="Product video preview of a trading chart">
    <svg class="abs play" viewBox="0 0 32 32"><path d="M13 10l9 6-9 6z" fill="#fff"/></svg>
  </div>
  <ul class="abs bullets" style="left:286px;top:713px;line-height:16.2px">
    <li>Features</li><li>Screenshots</li><li>Demo Instellation</li><li>Open Source Edition</li>
  </ul>
  <ul class="abs bullets" style="left:380px;top:713px;line-height:16.2px">
    <li>Third &nbsp;&nbsp;&nbsp;party<br>Libraries</li>
  </ul>
  <p class="abs small" style="left:286px;top:781px;width:169px">Duis ut justo lorem. Suspendisse eleifend, magna non sollicitudin tincidunt, urna mauris adipiscing mauris, eget eleifend magna elit eu</p>
  <div class="abs divider" style="left:475px;top:590px;height:225px"></div>

  <h2 class="abs" style="left:486px;top:590px">Testimonials</h2>
  <svg class="abs" style="left:635px;top:591px" width="28" height="11" viewBox="0 0 28 11"><circle cx="5.5" cy="5.5" r="5.5" fill="#666"/><circle cx="21.5" cy="5.5" r="5.5" fill="#666"/><path d="M6.5 3 4 5.5 6.5 8M20.5 3 23 5.5 20.5 8" fill="none" stroke="#fff" stroke-width="1.3"/></svg>
  <div class="abs testi" style="left:489px;top:619px"><p>“Sed ut perspiciatis unde omnis iste natus error sit voluptatem accusantium doloremque”</p><p class="who">- name of the client</p></div>
  <div class="abs photo" style="left:610px;top:622px" role="img" aria-label="Client portrait"></div>
  <div class="abs testi" style="left:489px;top:691px"><p>“Sed ut perspiciatis unde omnis iste natus error sit voluptatem accusantium doloremque”</p><p class="who">- name of the client</p></div>
  <div class="abs photo" style="left:610px;top:694px" role="img" aria-label="Client portrait"></div>
  <div class="abs testi" style="left:489px;top:764px"><p>“Sed ut perspiciatis unde omnis iste natus error sit voluptatem accusantium doloremque”</p><p class="who">- name of the client</p></div>
  <div class="abs photo" style="left:610px;top:767px" role="img" aria-label="Client portrait"></div>
</section>

<section class="lower">
  <h2 class="abs" style="left:65px;top:856px;color:var(--olive);font-size:12px">Documentation and Demo</h2>
  <p class="abs small" style="left:66px;top:879px;width:181px;line-height:12.5px">Proin lectus dui, eleifend sed aliquet nec, ultricies at urna. Ut egestas ligula non nibh gravida nec lobortis mauris rhoncus. Donec nibh sem, dignissim eget vulputate nec, adipiscing vel risus. Lorem ipsum dolor sit amet, consectetur.</p>
  <div class="abs btn" style="left:67px;top:946px">Know more</div>
  <div class="abs divider" style="left:269px;top:840px;height:140px"></div>

  <h2 class="abs" style="left:282px;top:853px">Professional Services</h2>
  <p class="abs small" style="left:281px;top:879px;width:180px;line-height:11.5px">Vivamus temporlan volutpat fermentum. Aliquam luctus, metus vel gravida rutrum, neque eros pel lentesque mauris, in convallis.</p>
  <div class="abs btn" style="left:279px;top:921px">Know more</div>
  <div class="abs divider" style="left:475px;top:840px;height:140px"></div>

  <h2 class="abs" style="left:493px;top:853px">Trainings</h2>
  <p class="abs small" style="left:493px;top:879px;width:180px;line-height:11.5px">Vivamus temporlan volutpat fermentum. Aliquam luctus, metus vel gravida rutrum, neque eros pel lentesque mauris, in convallis.</p>
  <div class="abs btn" style="left:492px;top:921px">Know more</div>
</section>

<section class="abs news">
  <h3>LATEST NEWS</h3>
  <div class="date">Feb<br>14</div>
  <p>Lorem ipsum dolor sit amet, consectetur adipisicing elit, sed do eiusmod tempor incididunt ut labore et dolore magna aliqua. Ut enim ad minim veniam, quis nostrud</p>
</section>

<footer>
  <div class="abs footer"></div>
  <p class="abs f-head" style="left:73px;top:1047px">Home</p>
  <p class="abs f-head" style="left:73px;top:1066px">Product</p>
  <div class="abs f-list" style="left:74px;top:1081px"><p>• Features</p><p>• Screen Shots</p><p>• Demo Installations</p><p>• Open Source Edition</p><p>• 3rd Party Libraries</p></div>

  <p class="abs f-head" style="left:173px;top:1047px">Documentation</p>
  <div class="abs f-list" style="left:174px;top:1062px"><p>• Reference</p><p>• PDF</p><p>• Online HTML</p><p>• Single Page HTML</p><p>• JavaDoc</p><p>• UML Model</p><p>• Release Notes</p></div>

  <p class="abs f-head" style="left:278px;top:1047px">Services &amp; Support</p>
  <div class="abs f-list" style="left:279px;top:1062px"><p>• &nbsp;Professional Services</p><p>• &nbsp;Training</p><p>• &nbsp;Forum</p></div>
  <p class="abs f-head" style="left:278px;top:1110px">Clients &amp; Partners</p>
  <p class="abs f-head" style="left:278px;top:1129px">News</p>
  <p class="abs f-head" style="left:278px;top:1151px">Site-Map</p>

  <p class="abs f-head" style="left:392px;top:1047px">About us</p>
  <p class="abs f-item" style="left:393px;top:1065px">• &nbsp;Team</p>
  <p class="abs f-item" style="left:396px;top:1094px">Address :</p>
  <p class="abs f-item" style="left:438px;top:1094px;line-height:11.5px">QuantoMesh<br>Lindenweg 42<br>CH-8050 Zürich</p>
  <p class="abs f-item" style="left:401px;top:1133px">Call us :</p>
  <p class="abs f-item" style="left:438px;top:1133px">+41 44 555 20 37</p>
  <p class="abs f-item" style="left:405px;top:1152px">Email :</p>
  <p class="abs f-item" style="left:438px;top:1152px">info@quantomesh-example.ch</p>

  <div class="abs divider" style="left:524px;top:1044px;height:120px;background:#7c8790"></div>
  <div class="abs f-brand"><span class="f-mark"></span>QuantoMesh</div>
  <p class="abs f-copy">Copyright © 2013 &nbsp;www.quantomesh-example.ch<br>All rights reserved.<br>Terms and Conditions &nbsp;| &nbsp;Privacy Policy</p>
  <div class="abs soc" style="left:545px" aria-label="Chatterwall"></div>
  <div class="abs soc" style="left:566px" aria-label="RSS Feed"><svg width="16" height="16" viewBox="0 0 16 16"><circle cx="6" cy="10" r="1" fill="#dfe3e6"/><path d="M5 7a4 4 0 0 1 4 4M5 5a6 6 0 0 1 6 6" fill="none" stroke="#dfe3e6" stroke-width="1.1"/></svg></div>
  <div class="abs soc" style="left:587px" aria-label="CareerWeave"></div>
  <div class="abs soc" style="left:608px" aria-label="Email"><svg width="16" height="16" viewBox="0 0 16 16"><rect x="4" y="5" width="8" height="6" fill="none" stroke="#dfe3e6"/><path d="M4 5l4 3.5L12 5" fill="none" stroke="#dfe3e6"/></svg></div>
</footer>
</body>
</html>
```